Update the A4 Specials Page for Restaurant/Cafe

Provide a MINIMALIST attractive Specials page we can print weekly for our food and drink specials to give to our guests. Final design is to be provided in WORD Document so it can be easily edited by Manager. Should be black text and MINIMALIST to minimise ink usage as we print hundreds a week. We have UPLOADED the existing page as a template for you to update. Maybe logo can stay, see what you think. Or delete it and do something else. Keep it simple. Choose a good FONT. Could be a little playful with a cocktail ICON or something. Our existing menus can be seen at www.tallowmillcafe.com.au and they are using font Alegreya. Please note we are unable to provide any feedback to designers, however we really do appreciate your time if you are submitting a design. Thank you for your participation.

```html
<!DOCTYPE html>
<html lang="en">
<head>
<meta charset="utf-8">
<title>Tallow Mill Cafe – Weekly Specials</title>
<link rel="stylesheet" href="https://fonts.googleapis.com/css2?family=Poppins:wght@400;500;600;700&display=swap">
<style>
  :root {
    --backdrop: #e6e7e8;
    --paper: #ffffff;
    --ink: #111111;
    --ink-soft: #4a4a4a;
    --band: #000000;
    --band-text: #ffffff;
  }
  * { margin: 0; padding: 0; box-sizing: border-box; }
  html, body {
    width: 676px;
    height: 1200px;
    overflow: hidden;
    background: var(--backdrop);
    font-family: "Poppins", sans-serif;
    color: var(--ink);
  }
  .specials-page {
    position: absolute;
    left: 0;
    top: 122px;
    width: 676px;
    height: 956px;
    background: var(--paper);
    box-shadow: 3px 4px 6px rgba(0,0,0,0.25);
  }
  .brand-band {
    position: absolute;
    left: 67px;
    top: 0;
    width: 50px;
    height: 191px;
    background: var(--band);
  }
  .brand-name {
    position: absolute;
    left: 50%;
    top: 50%;
    transform: translate(-50%, -50%) rotate(-90deg);
    white-space: nowrap;
    color: var(--band-text);
    font-size: 13px;
    font-weight: 600;
    letter-spacing: 0.04em;
  }
  .line {
    position: absolute;
    left: 0;
    width: 100%;
    text-align: center;
    line-height: 1;
    white-space: nowrap;
  }
  .section-title { font-size: 21px; font-weight: 600; letter-spacing: 0.16em; }
  .item-name { font-size: 19px; font-weight: 400; letter-spacing: 0.12em; }
  .item-name--soft { color: var(--ink-soft); }
  .item-detail { font-size: 12.5px; font-weight: 400; }
  .item-price { font-size: 19px; font-weight: 600; }
  .closing-rule {
    position: absolute;
    left: 267px;
    top: 878px;
    width: 140px;
    height: 3px;
    background: var(--ink);
  }
</style>
</head>
<body>
  <main class="specials-page">
    <div class="brand-band"><span class="brand-name">TALLOW MILL CAFE</span></div>

    <h1 class="line section-title" style="top:157px">WEEKLY SPECIALS</h1>
    <h2 class="line item-name" style="top:202px">CHICKEN FILO</h2>
    <p class="line item-detail" style="top:234px">Creamy Chicken with Pinenuts. wrapped in Filo Pastry.</p>
    <p class="line item-detail" style="top:256px">Served with Side Salad &amp; Zulu Sauce</p>
    <p class="line item-price" style="top:284px">$24</p>

    <h2 class="line item-name" style="top:326px">MINESTRONE SOUP</h2>
    <p class="line item-detail" style="top:358px">Served with Garlic Bread</p>
    <p class="line item-price" style="top:386px">$8</p>

    <h1 class="line section-title" style="top:451px">COCKTAIL SPECIAL</h1>
    <h2 class="line item-name item-name--soft" style="top:495px">PASSIONISTA</h2>
    <p class="line item-detail" style="top:529px">Vodka, Passionfruit Pulp, Mango Puree</p>
    <p class="line item-detail" style="top:551px">Top up with Ginger &amp; Lemon Kombucha</p>
    <p class="line item-price" style="top:579px">$17</p>

    <h1 class="line section-title" style="top:643px">CRAFT BEER SPECIAL</h1>
    <h2 class="line item-name item-name--soft" style="top:687px">CROOKED GECKO</h2>
    <p class="line item-detail" style="top:720px">SUN BURST</p>
    <p class="line item-detail" style="top:741px">Tropical Pale Ale</p>
    <p class="line item-detail" style="top:763px">4.8% Alc.</p>
    <p class="line item-price" style="top:790px">$10</p>

    <div class="closing-rule"></div>
  </main>
</body>
</html>
```